Brightoak Business Card

Professional Business Card Design required using the attached contact information.

Contact information can be rearranged as required.

The company is a new start up venture developing solar systems, the branding should be in keeping with that of one of the investors whose website is as follows https://www.corvellan.com/

```html
<!DOCTYPE html>
<html lang="en">
<head>
<meta charset="utf-8">
<title>Brightoak Solar – Business Card</title>
<link rel="stylesheet" href="https://fonts.googleapis.com/css2?family=Montserrat:wght@400;600;700&display=swap">
<style>
  :root {
    --backdrop: #d9d6d0;
    --card-white: #ffffff;
    --card-shade: #ececec;
    --brand-green: #24725f;
    --brand-green-dark: #1d5f4f;
    --ink: #151515;
    --muted: #777777;
    --on-green: #ffffff;
  }
  * { box-sizing: border-box; margin: 0; padding: 0; }
  html, body { width: 1200px; height: 1136px; overflow: hidden; }
  body {
    background: var(--backdrop);
    font-family: "Montserrat", sans-serif;
    display: flex;
    flex-direction: column;
    align-items: center;
    justify-content: center;
    gap: 56px;
  }
  .card {
    width: 840px;
    height: 480px;
    border-radius: 4px;
    box-shadow: 0 10px 28px rgba(0,0,0,0.25);
    position: relative;
    overflow: hidden;
  }
  .card--front {
    background: radial-gradient(ellipse at 50% 60%, var(--card-white) 40%, var(--card-shade) 100%);
    display: flex;
    flex-direction: column;
    align-items: center;
    padding-top: 64px;
  }
  .card--back {
    background: radial-gradient(ellipse at 50% 40%, var(--brand-green) 55%, var(--brand-green-dark) 100%);
    display: flex;
    flex-direction: column;
    align-items: center;
    justify-content: center;
    gap: 40px;
  }
  .wordmark {
    display: flex;
    align-items: center;
    gap: 14px;
    white-space: nowrap;
    font-weight: 600;
    font-size: 40px;
    letter-spacing: 0;
    color: var(--ink);
  }
  .wordmark__dot {
    width: 16px; height: 16px;
    border-radius: 50%;
    background: var(--brand-green);
    flex: none;
  }
  .card--back .wordmark { color: var(--on-green); font-size: 48px; }
  .card--back .wordmark__dot { background: var(--on-green); }
  .contact { margin-top: 50px; width: 420px; }
  .contact__name {
    font-weight: 700;
    font-size: 34px;
    color: var(--brand-green);
  }
  .contact__company {
    font-weight: 600;
    font-size: 18px;
    color: var(--brand-green);
    margin-top: 14px;
  }
  .contact__address {
    font-size: 18px;
    color: var(--muted);
    margin-top: 6px;
  }
  .contact__lines { list-style: none; margin-top: 24px; }
  .contact__line {
    display: flex;
    align-items: center;
    gap: 10px;
    font-size: 18px;
    color: var(--muted);
    line-height: 1.6;
  }
  .contact__icon { width: 14px; height: 14px; fill: var(--brand-green); flex: none; }
  .card__url {
    font-size: 20px;
    color: var(--on-green);
    letter-spacing: 0.02em;
  }
</style>
</head>
<body>
  <section class="card card--front" aria-label="Business card front">
    <div class="wordmark"><span class="wordmark__dot"></span>Brightoak Solar</div>
    <div class="contact">
      <h1 class="contact__name">Daniel Hollis</h1>
      <p class="contact__company">Brightoak Solar LLC</p>
      <p class="contact__address">218 Harbor Street, Salem, MA 01970</p>
      <ul class="contact__lines">
        <li class="contact__line">
          <svg class="contact__icon" viewBox="0 0 24 24"><path d="M6.6 10.8a15.1 15.1 0 0 0 6.6 6.6l2.2-2.2c.3-.3.7-.4 1-.2 1.1.4 2.3.6 3.6.6.6 0 1 .4 1 1V20c0 .6-.4 1-1 1C10.6 21 3 13.4 3 4c0-.6.4-1 1-1h3.5c.6 0 1 .4 1 1 0 1.3.2 2.5.6 3.6.1.3 0 .7-.2 1z"/></svg>
          +1 (555) 014-2276
        </li>
        <li class="contact__line">
          <svg class="contact__icon" viewBox="0 0 24 24"><path d="M2 5h20v14H2z M3.5 6.5 12 13l8.5-6.5" fill="none" stroke="#24725f" stroke-width="2"/></svg>
          daniel.hollis@brightoak-solar.com
        </li>
        <li class="contact__line">
          <svg class="contact__icon" viewBox="0 0 24 24"><circle cx="12" cy="12" r="10"/></svg>
          www.brightoak-solar.com
        </li>
      </ul>
    </div>
  </section>

  <section class="card card--back" aria-label="Business card back">
    <div class="wordmark"><span class="wordmark__dot"></span>Brightoak Solar</div>
    <p class="card__url">www.brightoak-solar.com</p>
  </section>
</body>
</html>
```